Kid's Cancer Camp Business Card

Create a unique Two-Sided color business cards for Camp Willow Brook, a pediatric cancer camp.

The camp tag line is: A camp where every child finds joy...

Dale Morrisey, Executive Director
Camp Willow Brook Charitable Foundation, Inc
PO Box 918
Alder Falls, NY 06832

Phone - 203-555-0143
Fax - 203-555-0187
Email: dale@campwillowbrook.example
www.campwillowbrook.example

Target Market(s)

Potential Donors, Volunteers and Campers

Industry/Entity Type

Non-profit pediatric cancer camp

Contact Information for Business Card

All contact info that is included in the description

Font styles to use
Other font styles liked:
• Designer chooses font

Requirements
Must have
• Camp Willow Brook Logo and Tag Line
Nice to have
• should be eye catching
Should not have
• not cartoony

```html
<!DOCTYPE html>
<html lang="en">
<head>
<meta charset="utf-8">
<title>Camp Willow Brook – Business Card</title>
<link href="https://fonts.googleapis.com/css2?family=Poppins:wght@400;500;600&family=Kalam:wght@400&display=swap" rel="stylesheet">
<style>
  :root {
    --stage: #333333;
    --brand-blue: #036ba1;
    --sun-yellow: #f9b122;
    --teal: #0b9a8d;
    --ink-blue: #0a5f95;
    --paper: #ffffff;
  }
  html, body {
    margin: 0;
    padding: 0;
    width: 1053px;
    height: 1200px;
    overflow: hidden;
    background: var(--stage);
  }
  .canvas {
    width: 1053px;
    height: 1200px;
    display: flex;
    flex-direction: column;
    align-items: center;
    justify-content: center;
    gap: 56px;
  }
  .card {
    width: 860px;
    height: 516px;
    display: block;
    box-shadow: 0 18px 30px rgba(0,0,0,0.45);
    background: var(--paper);
  }
  .sans { font-family: "Poppins", Arial, sans-serif; }
  .script { font-family: "Kalam", cursive; }
  .wordmark { font-family: "Poppins", Arial, sans-serif; font-weight: 500; fill: var(--ink-blue); }
  .name-first { fill: var(--sun-yellow); font-weight: 600; }
  .name-last { fill: var(--paper); font-weight: 400; }
  .title { fill: var(--paper); font-size: 10.5px; }
  .contact { fill: var(--paper); font-size: 14.5px; }
  .org { fill: var(--sun-yellow); font-weight: 600; font-size: 14.5px; }
  .tagline { fill: var(--teal); font-size: 21px; }
  .icon-box { fill: none; stroke: var(--paper); stroke-width: 1.2; }
  .icon-line { fill: none; stroke: var(--paper); stroke-width: 1.1; stroke-linecap: round; }
</style>
</head>
<body>
<main class="canvas">

  <!-- Contact side -->
  <svg class="card card-front" viewBox="0 0 682 409" xmlns="http://www.w3.org/2000/svg">
    <rect width="682" height="409" fill="var(--paper)"/>
    <path class="swoosh-accent" d="M268 0 C360 80 440 250 445 409 H477 C470 250 385 80 278 0 Z" fill="var(--sun-yellow)"/>
    <path class="swoosh-panel" d="M0 0 H268 C360 80 440 250 445 409 H0 Z" fill="var(--brand-blue)"/>

    <text class="sans" x="45" y="92" font-size="21"><tspan class="name-first">DALE</tspan><tspan class="name-last"> MORRISEY</tspan></text>
    <text class="sans title" x="45" y="110">EXECUTIVE DIRECTOR</text>

    <!-- phone -->
    <rect class="icon-box" x="46" y="198" width="13" height="13" rx="2"/>
    <path class="icon-line" d="M49.5 201.5 q0.5 4 5.5 6.5 l1.5 -1.5 -2 -1.5 -1 1 q-2 -1 -2.5 -2.5 l1 -1 -1.3 -2 z"/>
    <text class="sans contact" x="68" y="210">203-555-0143</text>
    <!-- fax -->
    <rect class="icon-box" x="46" y="221" width="13" height="13" rx="2"/>
    <path class="icon-line" d="M49 231 v-5 h7 v5 M50.5 226 v-2.5 h4 v2.5"/>
    <text class="sans contact" x="68" y="233">203-555-0187</text>
    <!-- email -->
    <rect class="icon-box" x="46" y="244" width="13" height="13" rx="2"/>
    <path class="icon-line" d="M49 248 h7 v5.5 h-7 z M49 248 l3.5 3 3.5 -3"/>
    <text class="sans contact" x="68" y="256">dale@campwillowbrook.example</text>
    <!-- web -->
    <rect class="icon-box" x="46" y="267" width="13" height="13" rx="2"/>
    <circle class="icon-line" cx="52.5" cy="273.5" r="3.8"/>
    <path class="icon-line" d="M48.7 273.5 h7.6 M52.5 269.7 v7.6"/>
    <text class="sans contact" x="68" y="279">www.campwillowbrook.example</text>

    <text class="sans org" x="45" y="318">CAMP WILLOW BROOK</text>
    <text class="sans contact" x="45" y="336">Charitable Foundation, Inc</text>
    <text class="sans contact" x="45" y="355">PO Box 918, Alder Falls, NY 06832</text>

    <g class="logo-small">
      <circle cx="448" cy="98" r="9" fill="var(--sun-yellow)"/>
      <text class="wordmark" x="463" y="104" font-size="17">Camp Willow Brook</text>
    </g>

    <text class="script tagline" x="460" y="240">A camp where</text>
    <text class="script tagline" x="475" y="286">every child</text>
    <text class="script tagline" x="490" y="332">finds joy...</text>
  </svg>

  <!-- Logo side -->
  <svg class="card card-back" viewBox="0 0 682 409" xmlns="http://www.w3.org/2000/svg">
    <rect width="682" height="409" fill="var(--paper)"/>
    <g class="logo-large">
      <circle cx="191" cy="205" r="17" fill="var(--sun-yellow)"/>
      <text class="wordmark" x="220" y="217" font-size="34">Camp Willow Brook</text>
    </g>
  </svg>

</main>
</body>
</html>
```